Orchard Bough Growing - Book Covers - Ebook, Paperback, Hardcover

Title would be:
Orchard Bough Growing
Subtitle: 7 Easy Stages Covering, Ground Choice, Blossom Care and Feeding, Trimming, Tiny Plots, Bug Management, Exotic Orchard Plants, and Vines
Author: Marlene Okafor
I would like the designer to have a couple of beautiful pictures on the cover. Please make it unique.
This would be posted on Quillora so please use specifications for book covers on Quillora
Back Cover should read:
Orchard Bough Growing
7 Easy Stages Covering, Ground Choice, Blossom Care and Feeding, Trimming, Tiny Plots, Bug Management, Exotic Orchard Plants, and Vines
Marlene Okafor
How to grow a thriving orchard and reap a bountiful harvest in less than a year – in both urban and non-urban settings
Fruit trees are fun to grow and will reward you with years of fresh, juicy homegrown produce.
However, the process can be excruciating, especially if you don’t know the best varieties to grow or how to control pests and diseases.
With a little planning and guidance, you will soon be biting into mellow fruits from trees in your backyard – including cherries, plums, pears, apples, and more.
All you need is to learn how to care for the trees, which you will find inside.
In Orchard Bough Growing, you’ll discover:
● How to pick the right fruit tree varieties for your growing zone and needs to ensure the plants don’t die
● How to effectively plan and prepare the planting site to lay a good foundation for your incoming trees
● How to choose the right irrigation system for your orchard and keep your fruit trees nourished all year long
● Examples of fruit garden plans for different regions – including a guide to help you design your small backyard space
● How to plant fruits to ensure proper pollination, fertilization, and flourishing growth of your produce
● Different fruit tree propagation methods with step-by-step instructions to help you grow your trees without spending money on costly grafts
● When and how to harvest fruits to ensure you collect them at their best and prevent wasting your hard work
● How to boost fruit production, encourage growth, and protect your trees from dangerous diseases
● How to look after fruit trees during all seasons, practice organic farming, and control pests in your garden
And much more…
It’s time to grow your mini-orchard and bask in years of harvest and sweetness from your labor.
Discover how you can have a thriving orchard and a bountiful fruit harvest.
Updates
Hello all Designers,
Please include this on the back cover as I forgot to include it in my main project:
Back Cover to read:
Orchard Bough Growing
Marlene Okafor
And much more…
Target Market(s)
People Who Love Gardening
Industry/Entity Type
Publishing
Requirements
Must have
- Title, Subtitle, Author Name, Beautiful Design, Eye Catching making you want to buy the book
Nice to have
- Large title, Easy to read subtitle intriguing pictures
Should not have
- Busy with too much stuff going on

```html
<!DOCTYPE html>
<html lang="en">
<head>
<meta charset="utf-8">
<title>Orchard Bough Growing – Cover</title>
<link rel="stylesheet" href="https://fonts.googleapis.com/css2?family=Bebas+Neue&family=Oswald:wght@500;600&display=swap">
<style>
  :root {
    --page-bg: #ecebea;
    --soil-light: #b29c78;
    --soil-mid: #5e4a33;
    --soil-dark: #2a2015;
    --leaf-light: #c7d87a;
    --leaf-deep: #4f7a2a;
    --sky-glow: #f3f1d2;
    --fruit-orange: #e9792a;
    --crate-wood: #a88c68;
    --ink-dark: #241a12;
    --title-white: #f7f6f3;
  }
  * { margin: 0; padding: 0; box-sizing: border-box; }
  html, body { width: 1200px; height: 1200px; overflow: hidden; }
  body { background: var(--page-bg); position: relative; }

  .book-cover {
    position: absolute;
    left: 244px; top: 50px;
    width: 712px; height: 1100px;
    overflow: hidden;
    background: linear-gradient(180deg, var(--soil-light) 0%, var(--soil-mid) 20%, var(--soil-dark) 45%, var(--soil-dark) 100%);
    box-shadow: 0 14px 40px rgba(0,0,0,.25);
  }

  .orchard-photo {
    position: absolute;
    left: 0; top: 0; width: 100%; height: 590px;
    background:
      radial-gradient(ellipse 46% 14% at 54% 43%, rgba(233,121,42,.95) 0%, rgba(233,121,42,.7) 55%, rgba(233,121,42,0) 100%),
      linear-gradient(180deg, rgba(0,0,0,0) 46%, var(--crate-wood) 56%, #8a7050 78%, rgba(178,156,120,0) 100%),
      radial-gradient(ellipse 32% 30% at 48% 18%, var(--sky-glow) 0%, rgba(243,241,210,0) 100%),
      linear-gradient(90deg, var(--leaf-deep) 0%, var(--leaf-light) 35%, var(--leaf-light) 62%, #8fae45 85%, #c9873a 100%);
  }
  .orchard-photo::after {
    content: "";
    position: absolute; left: 0; right: 0; bottom: 0; height: 90px;
    background: linear-gradient(180deg, rgba(178,156,120,0) 0%, var(--soil-light) 100%);
  }

  .author-name {
    position: absolute; top: 36px; left: 0; width: 100%;
    text-align: center;
    font-family: "Oswald", sans-serif; font-weight: 600;
    font-size: 30px; letter-spacing: 7px;
    color: var(--ink-dark);
  }

  .subtitle {
    position: absolute; left: 70px; width: 560px; top: 305px;
    text-align: center;
    font-family: "Oswald", sans-serif; font-weight: 600;
    color: var(--ink-dark);
  }
  .subtitle-lead { font-size: 27px; letter-spacing: 4px; margin-bottom: 16px; }
  .subtitle-list { font-size: 17.5px; line-height: 34px; letter-spacing: .2px; }

  .title {
    position: absolute; top: 520px; left: 0; width: 100%;
    text-align: center;
    font-family: "Bebas Neue", sans-serif;
    color: var(--title-white);
  }
  .title-main { display: block; font-size: 240px; line-height: 212px; letter-spacing: 2px; }
  .title-sub {
    display: block; margin-top: 26px;
    font-size: 70px; line-height: 70px; letter-spacing: 41px;
    padding-left: 41px;
  }
</style>
</head>
<body>
  <div class="book-cover">
    <div class="orchard-photo" role="img" aria-label="Sunlit orange orchard with a wooden crate full of ripe citrus fruit on a rustic table"></div>

    <p class="author-name">MARLENE OKAFOR</p>

    <div class="subtitle">
      <p class="subtitle-lead">7 EASY STAGES COVERING</p>
      <p class="subtitle-list">GROUND CHOICE, BLOSSOM CARE AND FEEDING, TRIMMING,<br>TINY PLOTS, BUG MANAGEMENT, EXOTIC ORCHARD PLANTS, AND VINES</p>
    </div>

    <h1 class="title">
      <span class="title-main">ORCHARD</span>
      <span class="title-main">BOUGH</span>
      <span class="title-sub">GROWING</span>
    </h1>
  </div>
</body>
</html>
```